Biz Card Design BTPW

New business card for a new company.
Logo was completed by a designer on ArtFlock and looking to continue requesting additional services.
Company Name: Bright Tidal Power Works
Although this company is starting in Canada, we will be moving towards a global presence within the next 6 months.
Key elements to this business are as follows.
Energy Procurement
Energy Reduction Services
Demand Side Consulting
Energy Efficiency Consulting
Saving Clients Money
Helping Them Go "Green"
Managing Their Energy Requirements
Basically the goal for our company is to find the best procurement solution for our clients and reduce their energy consumption. This reduces their expenses and the amount of greenhouse gas they produce on a daily basis.
I have been in the energy footprint for the last 20 years and know that most companies are looking to "do whatever is necessary to get them to sign on the dotted line". I would prefer to walk away from a client that I can't help than to put them into a situation that they will regret for years to come. This is where the "BRIGHT" part of the company name comes from.
The following is a catch phrase that encompasses what we do.
"Reducing your carbon footprint & energy bill at the same time!"
The back of the card needs to have this statement along with some sort of illustration. The back is a playground for creative ideas.
The front of the card needs the following.
Logo.
First & Last Name (Ned Varsolo)
Title (Energy Warrior)
Phone Number (555) 314-2769
Fax Number (555) 871-4420
Email Address ned@brighttidalpowerworks.example
Address 47 elmwick ave Toronto Ontario K2K 2K2
I want it to be a card that is remembered when any of my staff give it to a customer. It HAS to stand out.
Target Market(s)
Business Owners, Decision Makers, 30 to 65+
Industry/Entity Type
Business
Look and feel
Each slider illustrates characteristics of the customer's brand and the style your logo design should communicate.

```html
<!DOCTYPE html>
<html lang="en">
<head>
<meta charset="utf-8">
<title>Bright Tidal Power Works – Business Card</title>
<link href="https://fonts.googleapis.com/css2?family=Roboto+Condensed:wght@400;700&family=Poppins:wght@600&display=swap" rel="stylesheet">
<style>
  :root {
    --bg: #e9e7e3;
    --card: #ffffff;
    --green: #3aa83f;
    --green-light: #7fcf6a;
    --blue: #2f6cc0;
    --rule: #9bb6e0;
    --ink: #1f1f1f;
    --grey: #5a5a5a;
    --footprint-dark: #3a3a3a;
  }
  * { margin: 0; padding: 0; box-sizing: border-box; }
  html, body { width: 1200px; height: 900px; overflow: hidden; }
  body {
    background: var(--bg);
    font-family: "Roboto Condensed", "Arial Narrow", sans-serif;
    color: var(--ink);
    position: relative;
  }
  .card {
    position: absolute;
    left: 320px;
    width: 560px;
    height: 320px;
    background: var(--card);
    box-shadow: 0 6px 18px rgba(0,0,0,.18);
  }
  .card--back { top: 110px; }
  .card--front { top: 470px; }

  /* back */
  .tagline {
    position: absolute;
    left: 34px; top: 30px;
    width: 420px;
    font-weight: 700;
    font-size: 23px;
    line-height: 1.15;
    letter-spacing: 1.5px;
    text-transform: uppercase;
  }
  .tagline .quote { color: var(--green); }
  .tagline .carbon { color: var(--grey); }
  .tagline .energy { color: var(--green); }
  .footprint-trail {
    position: absolute;
    left: 34px; top: 110px;
    width: 490px; height: 170px;
    background: linear-gradient(100deg, var(--footprint-dark) 0%, #6b8f66 45%, var(--green) 100%);
    opacity: .85;
    border-radius: 4px;
  }
  .back-brand {
    position: absolute;
    right: 34px; bottom: 18px;
    font-family: "Poppins", sans-serif;
    font-weight: 600;
    font-size: 13px;
    color: var(--blue);
  }

  /* front */
  .brand {
    position: absolute;
    left: 40px; top: 40px;
    display: flex; align-items: center; gap: 12px;
  }
  .brand-dot {
    width: 34px; height: 34px; border-radius: 50%;
    background: var(--green);
  }
  .brand-name {
    font-family: "Poppins", sans-serif;
    font-weight: 600;
    font-size: 27px;
    color: var(--blue);
    letter-spacing: -.5px;
  }
  .brand-rule {
    position: absolute;
    left: 40px; top: 96px;
    width: 480px; height: 1px;
    background: var(--rule);
  }
  .person {
    position: absolute;
    right: 40px; top: 124px;
    text-align: right;
    text-transform: uppercase;
  }
  .person-name { font-weight: 700; font-size: 22px; letter-spacing: .5px; }
  .person-title { font-size: 11px; letter-spacing: 1px; color: var(--grey); }
  .contacts {
    position: absolute;
    left: 40px; top: 180px;
    display: grid;
    grid-template-columns: auto auto;
    gap: 10px 26px;
    font-weight: 700;
    font-size: 15px;
    text-transform: uppercase;
    letter-spacing: .5px;
  }
  .contact { display: flex; align-items: center; gap: 8px; }
  .contact--email { grid-column: 1 / span 2; }
  .contact svg { width: 15px; height: 15px; fill: var(--green); flex: none; }
  .address {
    position: absolute;
    left: 40px; bottom: 24px;
    font-weight: 700;
    font-size: 15px;
    letter-spacing: .8px;
    text-transform: uppercase;
    color: var(--green);
  }
</style>
</head>
<body>

<section class="card card--back" aria-label="Card back">
  <p class="tagline"><span class="quote">“</span>Reducing your <span class="carbon">carbon</span> footprint &amp; <span class="energy">energy</span> bill at the same time!<span class="quote">”</span></p>
  <div class="footprint-trail" role="img" aria-label="Illustration of a trail of footprints turning from dark grey to green and into dollar signs"></div>
  <p class="back-brand">Bright Tidal Power Works</p>
</section>

<section class="card card--front" aria-label="Card front">
  <div class="brand">
    <span class="brand-dot"></span>
    <span class="brand-name">Bright Tidal Power Works</span>
  </div>
  <div class="brand-rule"></div>

  <div class="person">
    <p class="person-name">Ned Varsolo</p>
    <p class="person-title">Energy Warrior</p>
  </div>

  <div class="contacts">
    <p class="contact">
      <svg viewBox="0 0 16 16" aria-hidden="true"><rect x="4" y="1" width="8" height="14" rx="1.5"/><rect x="5.5" y="3" width="5" height="6" fill="#fff"/></svg>
      (555) 314-2769
    </p>
    <p class="contact">
      <svg viewBox="0 0 16 16" aria-hidden="true"><rect x="4" y="1" width="8" height="5"/><rect x="1" y="6" width="14" height="7" rx="1"/><rect x="4" y="11" width="8" height="4" fill="#fff" stroke="#3aa83f"/></svg>
      (555) 871-4420
    </p>
    <p class="contact contact--email">
      <svg viewBox="0 0 16 16" aria-hidden="true"><path d="M1 4h14v9H1z"/><path d="M1 4l7 5 7-5" fill="none" stroke="#fff" stroke-width="1.3"/></svg>
      ned@brighttidalpowerworks.example
    </p>
  </div>

  <p class="address">47 elmwick ave Toronto Ontario K2K 2K2</p>
</section>

</body>
</html>
```